Bref créative
Home provement Flyer/Door hanger
Kitchen,bathroom,windows
Im looking to make flyer or door hanger for home improvement company. I was thinking front side with kitchen & bathroom.
Back side windows.
Construction
Professional, corporate,
Tallow Ridge Builders, LLC
4817 Copper Fern RD
Suite 812
Vienna, VA 22182
Tel: 571 238 6054
www.tallowridgebuilders.example
We offer Financing
Free Estimate
I need the design to be on AI, EPS AND PSD FILE. I need them by each layer so i can edit later if i need to.
This is the company logo.
You may visit www.tallowridgebuilders.example and choose a right picture from the gallery

```html
<!DOCTYPE html>
<html lang="en">
<head>
<meta charset="utf-8">
<title>Tallow Ridge Builders – Door Hanger</title>
<link rel="stylesheet" href="https://fonts.googleapis.com/css2?family=Open+Sans:ital,wght@0,400;0,600;0,700;0,800;1,700&display=swap">
<style>
  :root {
    --page: #2a2b2c;
    --white: #ffffff;
    --paper-shade: #eef0ee;
    --green: #6cbf1e;
    --green-dark: #3f8a0c;
    --green-light: #a4e04a;
    --ink: #4a4a4a;
    --ink-soft: #6b6b6b;
    --black: #0f1010;
    --black-soft: #262828;
    --photo-warm: #b58a5e;
    --photo-cool: #9aa7b0;
  }
  * { box-sizing: border-box; margin: 0; padding: 0; }
  html, body { width: 1200px; height: 701px; overflow: hidden; }
  body {
    background: var(--page);
    font-family: "Open Sans", Arial, sans-serif;
    position: relative;
  }
  .hanger {
    position: absolute;
    top: 30px;
    width: 290px;
    height: 641px;
    border-radius: 10px;
    overflow: hidden;
    background: linear-gradient(180deg, var(--white) 0%, var(--white) 55%, var(--paper-shade) 75%);
    display: flex;
    flex-direction: column;
  }
  .hanger--back { left: 265px; }
  .hanger--front { left: 645px; }

  .hanger__hole {
    position: absolute;
    top: 28px;
    left: 50%;
    width: 84px;
    height: 84px;
    margin-left: -42px;
    border-radius: 50%;
    background: var(--page);
    border: 5px solid var(--green);
    box-shadow: 0 0 0 3px var(--green-dark), inset 0 0 0 2px var(--green-light);
  }
  .hanger__swoosh {
    position: absolute;
    top: 0; left: 0;
    width: 290px; height: 150px;
  }
  .hanger__body {
    position: relative;
    padding: 140px 18px 0;
    flex: 1;
  }
  .intro {
    font-size: 9.5px;
    line-height: 1.45;
    color: var(--ink);
    text-align: center;
  }
  .hanger--back .intro { padding-top: 6px; text-align: left; }

  .welcome {
    text-align: center;
    color: var(--green);
    font-weight: 800;
    line-height: 1.05;
    margin-bottom: 8px;
  }
  .welcome__small { display: block; font-size: 22px; }
  .welcome__name { display: block; font-size: 25px; }

  .section-row {
    display: flex;
    align-items: center;
    justify-content: space-between;
    margin: 12px 0 8px;
  }
  .section-title {
    font-size: 22px;
    font-weight: 800;
    color: var(--green);
    letter-spacing: -0.3px;
  }
  .hanger--front .section-title { text-align: center; margin: 12px 0 8px; }
  .offer-badge {
    background: var(--green);
    color: var(--white);
    font-size: 10px;
    font-weight: 700;
    line-height: 1.15;
    padding: 5px 9px;
    border-radius: 4px;
    text-align: center;
  }

  .photo-grid {
    display: grid;
    grid-template-columns: 1fr 1fr;
    grid-template-rows: 86px 86px;
    gap: 5px;
  }
  .photo {
    border-radius: 2px;
    border: 2px solid var(--white);
    box-shadow: 0 1px 4px rgba(0,0,0,.35);
  }
  .photo--window-white { background: linear-gradient(160deg, #e5e7e8, var(--photo-cool)); }
  .photo--window-red { background: linear-gradient(160deg, #9b3a2c, #d7a07c); }
  .photo--house { background: linear-gradient(180deg, #c8d7e2 0%, #e9e6df 55%, #7a8a5a 100%); }
  .photo--interior { background: linear-gradient(160deg, #6f5a48, #c9b79f); }

  .showcase {
    position: relative;
    height: 180px;
    border: 2px solid var(--white);
    box-shadow: 0 1px 5px rgba(0,0,0,.35);
    background: linear-gradient(135deg, #5a3e2a 0%, var(--photo-warm) 45%, #e6dccd 100%);
  }
  .price-tag {
    position: absolute;
    background: var(--green);
    color: var(--white);
    font-size: 9px;
    font-weight: 700;
    padding: 3px 7px;
    border-radius: 3px;
  }
  .price-tag--kitchen { top: 10px; left: 10px; }
  .price-tag--bath { bottom: 12px; left: 10px; }

  .band {
    margin-top: auto;
    height: 34px;
    background: linear-gradient(180deg, var(--green-light) 0%, var(--green) 45%, var(--green-dark) 100%);
    color: var(--white);
    font-weight: 700;
    font-style: italic;
    font-size: 16px;
    display: flex;
    align-items: center;
    justify-content: center;
  }
  .hanger--front .band { font-style: normal; font-size: 17px; }
  .footer {
    height: 116px;
    background: linear-gradient(180deg, var(--black-soft), var(--black));
    color: #cfcfcf;
    text-align: center;
    display: flex;
    flex-direction: column;
    justify-content: center;
    align-items: center;
  }
  .contact { font-size: 9px; line-height: 1.5; }
  .website {
    margin-top: 10px;
    font-size: 11px;
    font-weight: 700;
    color: var(--white);
  }
  .brand {
    display: flex;
    align-items: center;
    gap: 8px;
  }
  .brand__mark {
    width: 14px; height: 14px;
    background: var(--green);
  }
  .brand__name {
    font-size: 18px;
    font-weight: 700;
    color: var(--white);
    letter-spacing: 1px;
    text-transform: uppercase;
  }
</style>
</head>
<body>

  <!-- Back side: windows -->
  <article class="hanger hanger--back">
    <svg class="hanger__swoosh" viewBox="0 0 290 150" aria-hidden="true">
      <path d="M0 118 C 80 150, 200 150, 290 100 L290 112 C 200 160, 80 160, 0 130 Z" fill="var(--green)" opacity="0.25"/>
    </svg>
    <div class="hanger__hole"></div>
    <div class="hanger__body">
      <p class="intro">At Tallow Ridge Builders, LLC your goals for your home become our commitment. We tailor every project to your family and budget, from the first sketch to the final walkthrough, so each space works beautifully for years to come. Call today for your free first-time consultation.</p>
      <div class="section-row">
        <h2 class="section-title">Windows</h2>
        <div class="offer-badge">Buy 2 get<br>1 window free</div>
      </div>
      <div class="photo-grid">
        <div class="photo photo--window-white" role="img" aria-label="Photo of a white casement window installation"></div>
        <div class="photo photo--window-red" role="img" aria-label="Photo of a large glass window on a red wall"></div>
        <div class="photo photo--house" role="img" aria-label="Photo of a house exterior with new windows"></div>
        <div class="photo photo--interior" role="img" aria-label="Photo of an interior room with large windows"></div>
      </div>
    </div>
    <div class="band">We offer Financing</div>
    <footer class="footer">
      <p class="contact">Tallow Ridge Builders, LLC<br>4817 Copper Fern RD<br>Suite 812<br>Vienna, VA 22182<br>Tel: 571 238 6054</p>
      <p class="website">www.tallowridgebuilders.example</p>
    </footer>
  </article>

  <!-- Front side: kitchen & bathroom -->
  <article class="hanger hanger--front">
    <svg class="hanger__swoosh" viewBox="0 0 290 150" aria-hidden="true">
      <path d="M0 118 C 80 150, 200 150, 290 100 L290 112 C 200 160, 80 160, 0 130 Z" fill="var(--green)" opacity="0.25"/>
    </svg>
    <div class="hanger__hole"></div>
    <div class="hanger__body">
      <h1 class="welcome">
        <span class="welcome__small">Welcome to</span>
        <span class="welcome__name">Tallow Ridge</span>
      </h1>
      <p class="intro">Based out of northern Virginia, Tallow Ridge Builders, LLC has been dominating innovative bathroom remodels, kitchen remodels, home additions and more.</p>
      <h2 class="section-title">Kitchen &amp; Bathroom</h2>
      <div class="showcase" role="img" aria-label="Photos of a remodeled wooden kitchen and a bathroom with a freestanding tub">
        <span class="price-tag price-tag--kitchen">$8900 Installed</span>
        <span class="price-tag price-tag--bath">$7900 Installed</span>
      </div>
    </div>
    <div class="band">Free Estimate</div>
    <footer class="footer">
      <div class="brand">
        <span class="brand__mark"></span>
        <span class="brand__name">Tallow Ridge</span>
      </div>
    </footer>
  </article>

</body>
</html>
```